Vantora plinth system based website for technology jobs website

We need a website design for a technology job listing website, mainly aiming at 20/30/40 year old nerds. Jobs listed from multiple sources will be concatenated and organised. This website will be built with Vantora plinth system (https://plinthkit.example/manual/) so please use their components. The design should be simple and clear, so a user can directly look for offerings that are interesting for him.

Three different pages will be needed:

1. Main jobs list page

Contains a large table (https://plinthkit.example/manual/parts/grid-views.html#grid-views-anatomy), on top or next to this data-table users should be able to apply filters (select countries, select salary ranges) and somewhere an overview of the selected filters should be shown.

- A subscribe bar should be shown somewhere to allow a user to register for weekly/monthly mailings for new job offers with his preferred search filters.

2. Selected item page

If an item is clicked, a user should be able to view a job posting and it's details.

3. An advertiser should be able post his job offer.
Similar fields as https://post.ledgerworkboard.example/.
(https://plinthkit.example/manual/parts/input-boxes.html#input-boxes-arrangement)

Target Market(s)

20/30/40 year old nerds.

Industry/Entity Type

Computer

Logo Text

QuarkHire.io

Number of Pages Required

3 page

Colors

Designer to choose colors to be used in the design.

Requirements
Must have
• 1. Main jobs list page
• Contains a large table (https://plinthkit.example/manual/parts/grid-views.html#grid-views-anatomy), on top or next to this data-table users should be able to apply filters (select countries, select salary ranges) and somewhere an overview of the selected filters should be shown.
• - A subscribe bar should be shown somewhere to allow a user to register for weekly/monthly mailings for new job offers with his preferred search filters.
• 2. Selected item page
• If an item is clicked, a user should be able to view a job posting and it's details.
• 3. An advertiser should be able post his job offer,
• (https://plinthkit.example/manual/parts/input-boxes.html#input-boxes-arrangement)
• Please use open fonts!

```html
<!DOCTYPE html>
<html lang="en">
<head>
<meta charset="utf-8">
<title>QuarkHire.io – Job List</title>
<link href="https://fonts.googleapis.com/css2?family=Lato:wght@400;700&display=swap" rel="stylesheet">
<style>
  :root {
    --teal-dark: #137a80;
    --teal: #1c9ca3;
    --teal-light: #2bb3b3;
    --teal-text: #1a8a90;
    --orange: #f7931e;
    --orange-light: #ffb22e;
    --ink: #333333;
    --grey: #555555;
    --line: #cfcfcf;
    --white: #ffffff;
  }
  * { box-sizing: border-box; margin: 0; padding: 0; }
  html, body { width: 697px; height: 1200px; overflow: hidden; background: var(--white); }
  body { position: relative; font-family: 'Lato', sans-serif; color: var(--ink); }
  .abs { position: absolute; }

  .hero { left: 0; top: 0; width: 697px; height: 366px;
    background: linear-gradient(180deg, var(--teal-dark) 0%, var(--teal) 55%, var(--teal-light) 100%); }
  .logo { left: 73px; top: 22px; font-size: 22px; color: var(--white); font-weight: 400; letter-spacing: .2px; }
  .nav a { position: absolute; top: 29px; font-size: 11px; color: var(--white); text-decoration: none; }
  .nav a.active { font-weight: 700; }
  .nav a.active::after { content: ""; position: absolute; left: 0; right: 0; top: 19px; height: 2px; background: var(--white); }
  .btn-outline { border: 1px solid var(--white); color: var(--white); font-size: 10px; display: flex; align-items: center; justify-content: center; height: 22px; }

  .hero-title { left: 0; width: 697px; top: 122px; text-align: center; color: var(--white); font-weight: 700; font-size: 31px; }
  .hero-sub { left: 0; width: 697px; top: 160px; text-align: center; color: var(--white); font-size: 19px; font-weight: 400; }
  .search { left: 160px; top: 198px; width: 368px; height: 33px; border: 1px solid rgba(255,255,255,.8); border-radius: 17px; background: rgba(10,60,70,.35); }
  .search-text { left: 32px; top: 9px; font-size: 11px; color: var(--white); }
  .find-btn { left: 293px; top: 4px; width: 69px; height: 24px; border-radius: 12px; background: var(--orange); color: var(--white); font-size: 10px; font-weight: 700; display: flex; align-items: center; justify-content: center; }

  .section-title { left: 0; width: 697px; top: 395px; text-align: center; font-size: 19px; font-weight: 400; color: var(--ink); }
  .filter-label { left: 158px; top: 449px; font-size: 12px; font-weight: 700; color: var(--grey); }
  .select { top: 446px; width: 115px; height: 22px; border: 1px solid var(--line); font-size: 8px; color: var(--ink); padding: 6px 9px; }
  .select svg { position: absolute; right: 8px; top: 8px; }
  .apply-btn { left: 458px; top: 446px; width: 70px; height: 22px; background: var(--teal); color: var(--white); font-size: 8.5px; display: flex; align-items: center; justify-content: center; }

  .jobs { left: 74px; top: 498px; width: 554px; border-collapse: collapse; }
  .jobs td { height: 47.75px; border: 1px solid var(--line); font-size: 9px; color: var(--grey); padding: 0; }
  .jobs .company { width: 120px; text-align: center; color: var(--teal-text); font-size: 10.5px; }
  .jobs .role { width: 119px; padding-left: 20px; }
  .jobs .designation { width: 110px; padding-left: 28px; }
  .jobs .location { padding-left: 22px; font-size: 10.5px; color: var(--grey); }
  .jobs .location svg { vertical-align: -2px; margin-right: 5px; }

  .post-btn { left: 295px; top: 906px; width: 110px; height: 31px; border: 1.5px solid var(--teal); border-radius: 16px; color: var(--teal); font-weight: 700; font-size: 12px; display: flex; align-items: center; justify-content: center; }

  .newsletter { left: 0; top: 955px; width: 697px; height: 165px;
    background: linear-gradient(90deg, var(--orange) 0%, var(--orange-light) 50%, var(--orange) 100%); }
  .news-title { left: 0; width: 697px; top: 990px; text-align: center; color: var(--white); font-size: 19px; font-weight: 400; }
  .news-sub { left: 0; width: 697px; top: 1018px; text-align: center; color: var(--white); font-size: 9px; opacity: .9; }
  .email { left: 134px; top: 1042px; width: 434px; height: 27px; border-radius: 14px; background: var(--white); }
  .email-text { left: 15px; top: 9px; font-size: 7.5px; color: var(--ink); }
  .email-btn { left: 343px; top: 4px; width: 85px; height: 19px; border-radius: 10px; background: var(--teal); color: var(--white); font-size: 8px; font-weight: 700; display: flex; align-items: center; justify-content: center; }

  .foot-nav a { position: absolute; top: 1140px; font-size: 11px; color: var(--ink); text-decoration: none; }
  .social { top: 1139px; width: 19px; height: 19px; border-radius: 50%; background: var(--teal); }
  .copyright { left: 71px; top: 1165px; font-size: 8px; color: var(--grey); }
</style>
</head>
<body>
  <header>
    <div class="abs hero" role="img" aria-label="Photo of job candidates waiting in a row of chairs, teal tinted"></div>
    <div class="abs logo">QuarkHire.io</div>
    <nav class="nav">
      <a style="left:222px">About</a>
      <a class="active" style="left:273px">Job List</a>
      <a style="left:334px">Job Offer</a>
      <a style="left:400px">Support</a>
      <a style="left:460px">Help</a>
    </nav>
    <div class="abs btn-outline" style="left:505px;top:25px;width:58px">Sign Up</div>
    <div class="abs btn-outline" style="left:570px;top:24px;width:58px">Log In</div>

    <svg class="abs" style="left:51px;top:175px" width="14" height="22" viewBox="0 0 14 22"><polyline points="11,2 3,11 11,20" fill="none" stroke="#fff" stroke-width="3"/></svg>
    <svg class="abs" style="left:636px;top:175px" width="14" height="22" viewBox="0 0 14 22"><polyline points="3,2 11,11 3,20" fill="none" stroke="#fff" stroke-width="3"/></svg>

    <h1 class="abs hero-title">Find Your Dream Job here</h1>
    <p class="abs hero-sub">Mauris vel lacus vitae felis vestibulum</p>
    <div class="abs search">
      <svg class="abs" style="left:13px;top:9px" width="14" height="14" viewBox="0 0 14 14"><circle cx="5.5" cy="5.5" r="4.2" fill="none" stroke="#fff" stroke-width="2"/><line x1="8.6" y1="8.6" x2="12.5" y2="12.5" stroke="#fff" stroke-width="2.2" stroke-linecap="round"/></svg>
      <span class="abs search-text">Type Job here</span>
      <div class="abs find-btn">Find Now</div>
    </div>
  </header>

  <main>
    <h2 class="abs section-title">Featured Job</h2>
    <div class="abs filter-label">Filter By:</div>
    <div class="abs select" style="left:219px">Select Countries
      <svg width="7" height="5" viewBox="0 0 7 5"><polyline points="0.5,0.5 3.5,4 6.5,0.5" fill="none" stroke="#777" stroke-width="1"/></svg></div>
    <div class="abs select" style="left:339px">Select Salary Range
      <svg width="7" height="5" viewBox="0 0 7 5"><polyline points="0.5,0.5 3.5,4 6.5,0.5" fill="none" stroke="#777" stroke-width="1"/></svg></div>
    <div class="abs apply-btn">Apply Now</div>

    <table class="abs jobs">
      <tr><td class="company">Company Name</td><td class="role">Web Designer</td><td class="designation">Designation</td><td class="location"><svg width="8" height="12" viewBox="0 0 8 12"><path d="M4 0a4 4 0 0 1 4 4c0 3-4 8-4 8S0 7 0 4a4 4 0 0 1 4-4z" fill="#999"/><circle cx="4" cy="4" r="1.5" fill="#fff"/></svg>Location City</td></tr>
      <tr><td class="company">Company Name</td><td class="role">Web Designer</td><td class="designation">Designation</td><td class="location"><svg width="8" height="12" viewBox="0 0 8 12"><path d="M4 0a4 4 0 0 1 4 4c0 3-4 8-4 8S0 7 0 4a4 4 0 0 1 4-4z" fill="#999"/><circle cx="4" cy="4" r="1.5" fill="#fff"/></svg>Location City</td></tr>
      <tr><td class="company">Company Name</td><td class="role">Web Designer</td><td class="designation">Designation</td><td class="location"><svg width="8" height="12" viewBox="0 0 8 12"><path d="M4 0a4 4 0 0 1 4 4c0 3-4 8-4 8S0 7 0 4a4 4 0 0 1 4-4z" fill="#999"/><circle cx="4" cy="4" r="1.5" fill="#fff"/></svg>Location City</td></tr>
      <tr><td class="company">Company Name</td><td class="role">Web Development</td><td class="designation">Designation</td><td class="location"><svg width="8" height="12" viewBox="0 0 8 12"><path d="M4 0a4 4 0 0 1 4 4c0 3-4 8-4 8S0 7 0 4a4 4 0 0 1 4-4z" fill="#999"/><circle cx="4" cy="4" r="1.5" fill="#fff"/></svg>Location City</td></tr>
      <tr><td class="company">Company Name</td><td class="role">Engineer</td><td class="designation">Designation</td><td class="location"><svg width="8" height="12" viewBox="0 0 8 12"><path d="M4 0a4 4 0 0 1 4 4c0 3-4 8-4 8S0 7 0 4a4 4 0 0 1 4-4z" fill="#999"/><circle cx="4" cy="4" r="1.5" fill="#fff"/></svg>Location City</td></tr>
      <tr><td class="company">Company Name</td><td class="role">Software Developer</td><td class="designation">Designation</td><td class="location"><svg width="8" height="12" viewBox="0 0 8 12"><path d="M4 0a4 4 0 0 1 4 4c0 3-4 8-4 8S0 7 0 4a4 4 0 0 1 4-4z" fill="#999"/><circle cx="4" cy="4" r="1.5" fill="#fff"/></svg>Location City</td></tr>
      <tr><td class="company">Company Name</td><td class="role">Web Designer</td><td class="designation">Designation</td><td class="location"><svg width="8" height="12" viewBox="0 0 8 12"><path d="M4 0a4 4 0 0 1 4 4c0 3-4 8-4 8S0 7 0 4a4 4 0 0 1 4-4z" fill="#999"/><circle cx="4" cy="4" r="1.5" fill="#fff"/></svg>Location City</td></tr>
      <tr><td class="company">Company Name</td><td class="role">Data Analyser</td><td class="designation">Designation</td><td class="location"><svg width="8" height="12" viewBox="0 0 8 12"><path d="M4 0a4 4 0 0 1 4 4c0 3-4 8-4 8S0 7 0 4a4 4 0 0 1 4-4z" fill="#999"/><circle cx="4" cy="4" r="1.5" fill="#fff"/></svg>Location City</td></tr>
    </table>

    <div class="abs post-btn">Post a Job</div>

    <section>
      <div class="abs newsletter" role="img" aria-label="Photo of smiling young people, orange tinted"></div>
      <h2 class="abs news-title">Subscribe Our Newsletters</h2>
      <p class="abs news-sub">Curabitur iaculis tempus eros Curabitur vel mi sit amet magna</p>
      <div class="abs email">
        <span class="abs email-text">Enter Your E-mail Address</span>
        <div class="abs email-btn">SIGN UP</div>
      </div>
    </section>
  </main>

  <footer>
    <nav class="foot-nav">
      <a style="left:71px">Home</a>
      <a style="left:121px">About</a>
      <a style="left:173px">Job List</a>
      <a style="left:230px">Job Offer</a>
      <a style="left:296px">Support</a>
      <a style="left:356px">Help</a>
    </nav>
    <div class="abs social" style="left:514px"></div>
    <div class="abs social" style="left:538px"></div>
    <div class="abs social" style="left:562px"></div>
    <div class="abs social" style="left:586px"></div>
    <div class="abs social" style="left:610px"></div>
    <p class="abs copyright">© 2018 Company Name &nbsp;All right reserved &nbsp;Terms of Use</p>
  </footer>
</body>
</html>
```